Brenner & Holloway Stationery

Greetings again. Now we've got an awesome logo, it's time to get the stationery to go with it. We require the following items of stationery:

- Business Card - Print Ready, all we need to do is change names and numbers and submit to printer.  Double sided with logo on one side and details on the other side. (85mm x 55mm)

- With Compliments Slip

- Letterhead - These will be preprinted pages that will then be used as pages.
(A4)

- Envelope - Business Size(Standard DL)

Target Market(s)

Essentially, this firm services clients facing criminal charges and/or seeking legal aid. The firm is also looking at taking on more white-collar crime cases.

Requirements
Must have
• - Same Design Cues & Colours as the Branding details attached

• - Address (as follows)

• Suite 8

• 262-268 Marlow St

• CALDERWOOD VIC 3188

• Phone: (03) 9482 6315

• Fax: (03) 9482 6840

• Web: www.brennerandholloway.example.au

• - Colour: Pantone 194 (Red)

```html
<!DOCTYPE html>
<html lang="en">
<head>
<meta charset="utf-8">
<title>Brenner &amp; Holloway Stationery</title>
<link href="https://fonts.googleapis.com/css2?family=Cinzel:wght@500&family=Tinos:wght@400;700&display=swap" rel="stylesheet">
<style>
  :root {
    --crimson: #ac003f;
    --ink: #111111;
    --stripe: #000000;
    --paper: #ffffff;
    --grey: #8a8a8a;
    --backdrop: #5f604c;
    --blush: #f3dde4;
  }
  * { box-sizing: border-box; margin: 0; padding: 0; }
  html, body { width: 1200px; height: 960px; overflow: hidden; }
  body {
    background: var(--backdrop);
    font-family: "Tinos", "Times New Roman", serif;
    color: var(--ink);
    position: relative;
  }
  .sheet {
    position: absolute;
    background: var(--paper);
    overflow: hidden;
    box-shadow: 0 4px 12px rgba(0,0,0,.35);
  }

  /* shared brand block */
  .brand { display: flex; align-items: center; }
  .brand-mark { border-radius: 50%; background: var(--crimson); flex: none; }
  .brand-divider { width: 1px; background: #9a9a9a; align-self: stretch; }
  .brand-name {
    font-family: "Cinzel", "Times New Roman", serif;
    font-weight: 500;
    color: var(--ink);
    line-height: 1;
    white-space: nowrap;
  }
  .brand-sub {
    font-family: "Cinzel", "Times New Roman", serif;
    font-weight: 500;
    color: var(--ink);
    letter-spacing: .12em;
    white-space: nowrap;
  }

  .footer-band {
    position: absolute; left: 0; right: 0; bottom: 0;
    background: var(--crimson);
    border-top: solid var(--stripe);
    color: var(--paper);
    text-align: center;
    letter-spacing: .08em;
    white-space: nowrap;
  }
  .address {
    text-align: right;
    color: var(--grey);
    line-height: 1.3;
    white-space: nowrap;
  }
  .address b { font-weight: 700; }
  .tagline {
    text-transform: uppercase;
    letter-spacing: .08em;
    color: var(--grey);
    white-space: nowrap;
  }

  /* letterhead */
  .letterhead { left: 560px; top: 40px; width: 600px; height: 848px; }
  .letterhead .brand { position: absolute; left: 30px; top: 20px; height: 40px; gap: 8px; }
  .letterhead .brand-mark { width: 40px; height: 40px; }
  .letterhead .brand-name { font-size: 13px; }
  .letterhead .brand-sub { font-size: 7px; margin-top: 2px; }
  .letterhead .tagline { position: absolute; right: 38px; top: 40px; font-size: 6px; text-align: right; line-height: 1.3; }
  .letterhead .head-rule { position: absolute; left: 85px; right: 38px; top: 59px; height: 1px; background: #a8a8a8; }
  .letterhead .address { position: absolute; right: 38px; top: 64px; font-size: 6.5px; }
  .letterhead .faint-disc {
    position: absolute; left: 160px; top: 300px; width: 340px; height: 340px;
    border-radius: 50%; background: var(--blush); opacity: .7;
  }
  .letterhead .footer-band { height: 24px; border-top-width: 3px; font-size: 10px; line-height: 21px; }

  /* envelope DL */
  .envelope { left: 40px; top: 40px; width: 480px; height: 240px; }
  .envelope .flap-band { position: absolute; left: 0; right: 0; top: 0; height: 36px; background: var(--crimson); }
  .envelope .flap-disc { position: absolute; left: 220px; top: 5px; width: 26px; height: 26px; border-radius: 50%; background: var(--paper); }
  .envelope .brand { position: absolute; left: 20px; top: 50px; height: 40px; gap: 8px; }
  .envelope .brand-mark { width: 40px; height: 40px; }
  .envelope .brand-name { font-size: 13px; }
  .envelope .brand-sub { font-size: 6.5px; margin-top: 2px; }
  .envelope .tagline { position: absolute; left: 76px; top: 96px; font-size: 5px; line-height: 1.3; }
  .envelope .address { position: absolute; left: 20px; top: 112px; text-align: left; color: var(--ink); font-size: 7px; }
  .envelope .footer-band { height: 22px; border-top-width: 3px; font-size: 9px; line-height: 19px; }

  /* compliments slip */
  .comp-slip { left: 40px; top: 310px; width: 480px; height: 226px; }
  .comp-slip .slip-title { position: absolute; left: 18px; top: 18px; font-size: 10px; font-weight: 400; letter-spacing: .03em; }
  .comp-slip .brand { position: absolute; right: 16px; top: 12px; height: 32px; gap: 7px; }
  .comp-slip .brand-mark { width: 32px; height: 32px; }
  .comp-slip .brand-name { font-size: 11px; }
  .comp-slip .brand-sub { font-size: 5.5px; margin-top: 2px; }
  .comp-slip .address { position: absolute; right: 16px; bottom: 30px; font-size: 5.5px; }
  .comp-slip .footer-band { height: 20px; border-top-width: 3px; font-size: 8px; line-height: 17px; }

  /* business cards */
  .card { top: 570px; width: 235px; height: 152px; }
  .card-front { left: 40px; }
  .card-back { left: 290px; }
  .card-front .front-stack { position: absolute; left: 0; right: 0; top: 20px; display: flex; flex-direction: column; align-items: center; }
  .card-front .brand-mark { width: 34px; height: 34px; margin-bottom: 8px; }
  .card-front .brand-name { font-size: 12px; }
  .card-front .brand-sub { font-size: 6px; margin-top: 3px; }
  .card-front .footer-band { height: 26px; border-top-width: 3px; font-size: 6.5px; line-height: 23px; }
  .card-back .brand { position: absolute; right: 12px; top: 12px; height: 22px; gap: 5px; }
  .card-back .brand-mark { width: 22px; height: 22px; }
  .card-back .brand-name { font-size: 8px; }
  .card-back .brand-sub { font-size: 4px; margin-top: 1px; }
  .card-back .person { position: absolute; left: 14px; top: 56px; }
  .card-back .person-name { font-size: 13px; font-weight: 700; }
  .card-back .person-role { font-size: 6.5px; letter-spacing: .04em; margin-top: 1px; }
  .card-back .address { position: absolute; right: 12px; top: 46px; font-size: 5px; color: var(--ink); }
  .card-back .footer-band { height: 26px; border-top-width: 3px; font-size: 4.5px; line-height: 1.35; padding-top: 4px; text-transform: uppercase; }
</style>
</head>
<body>

  <section class="sheet letterhead">
    <div class="faint-disc"></div>
    <div class="brand">
      <span class="brand-mark"></span>
      <span class="brand-divider"></span>
      <div>
        <div class="brand-name">BRENNER &amp; HOLLOWAY</div>
        <div class="brand-sub">BARRISTERS &amp; SOLICITORS</div>
      </div>
    </div>
    <p class="tagline">Principled, candid and dedicated legal counsel<br>for your commercial and private matters</p>
    <div class="head-rule"></div>
    <div class="address">
      Suite 8<br>262-268 Marlow St<br>CALDERWOOD VIC 3188<br>
      <b>Phone</b>: (03) 9482 6315<br><b>Fax</b>: (03) 9482 6840<br>
      <b>Web</b>: www.brennerandholloway.example.au
    </div>
    <div class="footer-band">www.brennerandholloway.example.au</div>
  </section>

  <section class="sheet envelope">
    <div class="flap-band"><span class="flap-disc"></span></div>
    <div class="brand">
      <span class="brand-mark"></span>
      <span class="brand-divider"></span>
      <div>
        <div class="brand-name">BRENNER &amp; HOLLOWAY</div>
        <div class="brand-sub">BARRISTERS &amp; SOLICITORS</div>
      </div>
    </div>
    <p class="tagline">Principled, candid and dedicated legal counsel<br>for your commercial and private matters</p>
    <div class="address">Suite 8<br>262-268 Marlow St<br>CALDERWOOD VIC 3188</div>
    <div class="footer-band">www.brennerandholloway.example.au</div>
  </section>

  <section class="sheet comp-slip">
    <h2 class="slip-title">WITH COMPLIMENTS</h2>
    <div class="brand">
      <span class="brand-mark"></span>
      <span class="brand-divider"></span>
      <div>
        <div class="brand-name">BRENNER &amp; HOLLOWAY</div>
        <div class="brand-sub">BARRISTERS &amp; SOLICITORS</div>
      </div>
    </div>
    <div class="address">
      Suite 8<br>262-268 Marlow St<br>CALDERWOOD VIC 3188<br>
      <b>Phone</b>: (03) 9482 6315<br><b>Fax</b>: (03) 9482 6840<br>
      <b>Web</b>: www.brennerandholloway.example.au
    </div>
    <div class="footer-band">www.brennerandholloway.example.au</div>
  </section>

  <section class="sheet card card-front">
    <div class="front-stack">
      <span class="brand-mark"></span>
      <div class="brand-name">BRENNER &amp; HOLLOWAY</div>
      <div class="brand-sub">BARRISTERS &amp; SOLICITORS</div>
    </div>
    <div class="footer-band">www.brennerandholloway.example.au</div>
  </section>

  <section class="sheet card card-back">
    <div class="brand">
      <span class="brand-mark"></span>
      <span class="brand-divider"></span>
      <div>
        <div class="brand-name">BRENNER &amp; HOLLOWAY</div>
        <div class="brand-sub">BARRISTERS &amp; SOLICITORS</div>
      </div>
    </div>
    <div class="person">
      <div class="person-name">John Doe</div>
      <div class="person-role">ATTORNEY AT LAW</div>
    </div>
    <div class="address">
      Suite 8<br>262-268 Marlow St<br>CALDERWOOD VIC 3188<br>
      <b>Phone</b>: (03) 9482 6315<br><b>Fax</b>: (03) 9482 6840<br>
      <b>Web</b>: www.brennerandholloway.example.au
    </div>
    <div class="footer-band">Principled, candid and dedicated legal counsel<br>for your commercial and private matters</div>
  </section>

</body>
</html>
```